Bold Flyer Needed for Bold Little Gym

We need a 1 page flyer created for our small boutique fitness facility, KorVesta, which highlights a new service we are offering.
We are now offering Red Light Therapy (RLT) to our members and I need a full color, 1 page flyer created that captures the eye of our members while highlighting the benefits and clearly stating the prices at the bottom of the page.
Flyer will be printed out on a standard 8.5" x 11" sheet of paper and should be laid out in a way that is easy to read. Landscape or Portrait layouts are both expectable.
We are using Quorvane Glow Therapy Lights TelaRix 700 Lamps as found here http://lnkzo.example/7QWPL4M
I have attached the text that should be included and our logo for branding of the flyer.
Thank you!

```html
<!DOCTYPE html>
<html lang="en">
<head>
<meta charset="utf-8">
<title>KorVesta Red Light Therapy Flyer</title>
<link rel="stylesheet" href="https://fonts.googleapis.com/css2?family=Roboto+Condensed:wght@400;700&family=Roboto:wght@400;500&display=swap">
<style>
:root{
  --yellow:#f7d000;
  --black:#000;
  --charcoal:#1f1f1f;
  --panel:#222;
  --white:#fff;
  --ink:#111;
}
*{margin:0;padding:0;box-sizing:border-box}
html,body{width:962px;height:1200px;overflow:hidden;background:var(--black)}
.flyer{position:relative;width:962px;height:1200px;background:var(--black);color:var(--white);font-family:'Roboto',sans-serif;overflow:hidden}
.abs{position:absolute}
.cond{font-family:'Roboto Condensed',sans-serif;font-weight:700}

.hero-art{left:0;top:0;width:962px;height:640px}
.intro-panel{left:0;top:118px;width:488px;height:269px;background:var(--charcoal)}

.brand{left:50px;top:24px}
.brand-name{font-family:'Roboto Condensed',sans-serif;font-weight:700;font-size:62px;line-height:1;color:var(--white);letter-spacing:1px}
.brand-tag{margin-top:6px;font-family:'Roboto',sans-serif;font-weight:500;font-size:9px;letter-spacing:2.4px;color:var(--yellow);padding-left:26px}

.headline{left:49px;top:141px;width:440px;font-size:27px;line-height:37px;color:var(--yellow);text-transform:uppercase;white-space:nowrap}
.intro{left:49px;width:430px;font-size:22px;line-height:26px;color:var(--white)}

.benefits-band{left:0;top:387px;width:488px;height:72px;background:var(--yellow)}
.benefits-title{left:51px;top:408px;font-size:27px;line-height:34px;color:var(--ink);letter-spacing:.3px}

.benefit{left:51px;width:440px}
.benefit-icon{position:absolute;left:0;top:0}
.benefit h3{margin-left:40px;font-family:'Roboto Condensed',sans-serif;font-weight:700;font-size:18px;line-height:22px;text-transform:uppercase}
.benefit p{margin-left:40px;margin-top:9px;font-family:'Roboto Condensed',sans-serif;font-size:14.5px;line-height:22px;max-width:380px}

.divider{width:2px;background:var(--yellow)}

.offer{border-radius:50%;background:var(--white);color:var(--ink);text-align:center}
.offer-first{left:458px;top:-13px;width:236px;height:236px;padding-top:31px}
.offer-first .lead{font-family:'Roboto Condensed',sans-serif;font-weight:700;font-size:18px;line-height:26px}
.offer-first .just{font-size:16px;line-height:20px;margin-top:2px}
.offer-first .price{font-family:'Roboto Condensed',sans-serif;font-weight:700;font-size:52px;color:var(--yellow);line-height:52px}
.offer-first .regular{font-size:18px;line-height:22px;margin-top:2px}
.offer-limited{left:609px;top:349px;width:240px;height:236px;padding:44px 36px 0}
.offer-limited .lead{font-family:'Roboto Condensed',sans-serif;font-weight:700;font-size:18px;line-height:26px}
.offer-limited p{font-size:13.5px;line-height:18.5px;margin-top:6px}

.why-title{left:575px;top:600px;font-size:27px;line-height:34px;color:var(--yellow)}
.reason{left:549px;width:300px;text-align:right}
.reason h3{font-family:'Roboto Condensed',sans-serif;font-weight:700;font-size:18px;line-height:22px;text-transform:uppercase}
.reason p{margin-top:9px;font-family:'Roboto Condensed',sans-serif;font-size:14.5px;line-height:22px}
.reason-icon{width:116px;height:116px;border-radius:50%;background:var(--panel);left:870px;display:flex;align-items:center;justify-content:flex-start;padding-left:20px}

.prices{left:532px;top:1033px;width:430px;height:120px}
.price-table{left:607px;top:1043px;border-collapse:collapse;font-family:'Roboto Condensed',sans-serif;font-size:15.5px}
.price-table td{height:25.6px;padding:0}
.price-table .item{width:146px}
.price-table .mem{width:105px;color:var(--yellow)}

.cta{left:0;top:1055px;width:530px;height:98px}
.cta-copy{left:49px;top:1070px;color:var(--ink)}
.cta-copy h4{font-family:'Roboto Condensed',sans-serif;font-weight:700;font-size:17px;line-height:22px}
.cta-copy .line{font-family:'Roboto Condensed',sans-serif;font-size:14.5px;line-height:18px;margin-top:6px}
.cta-copy .phone{font-family:'Roboto Condensed',sans-serif;font-weight:700;font-size:23px;line-height:28px}
.cta-copy .after{font-family:'Roboto Condensed',sans-serif;font-size:14.5px}

.footer{left:0;top:1153px;width:962px;height:47px;background:var(--black);display:flex;align-items:center;justify-content:center;gap:34px;font-family:'Roboto Condensed',sans-serif;font-weight:700;font-size:17px;text-transform:uppercase}
</style>
</head>
<body>
<main class="flyer">

  <svg class="abs hero-art" viewBox="0 0 962 640" aria-hidden="true">
    <circle cx="747" cy="237" r="310" fill="var(--yellow)"/>
    <circle cx="576" cy="105" r="132" fill="none" stroke="var(--yellow)" stroke-width="4"/>
  </svg>

  <div class="abs intro-panel"></div>

  <svg class="abs" style="left:0;top:0" width="962" height="640" role="img" aria-label="Photo of a man relaxing beside a glowing red light therapy panel">
    <defs>
      <radialGradient id="photoTone" cx="45%" cy="45%" r="70%">
        <stop offset="0" stop-color="#e07a6e"/>
        <stop offset=".5" stop-color="#8a3a44"/>
        <stop offset="1" stop-color="#3a2228"/>
      </radialGradient>
    </defs>
    <circle cx="775" cy="218" r="245" fill="url(#photoTone)"/>
  </svg>

  <svg class="abs" style="left:489px;top:252px" width="78" height="262" role="img" aria-label="Red light therapy panel product">
    <defs>
      <linearGradient id="panelTone" x1="0" y1="0" x2="1" y2="0">
        <stop offset="0" stop-color="#e8e8ea"/>
        <stop offset=".5" stop-color="#f06a6a"/>
        <stop offset="1" stop-color="#c9c9cc"/>
      </linearGradient>
    </defs>
    <rect x="2" y="2" width="72" height="256" rx="4" fill="url(#panelTone)"/>
  </svg>

  <div class="abs brand">
    <div class="brand-name">KorVesta</div>
    <div class="brand-tag">PERSONAL GROUP TRAINING</div>
  </div>

  <h1 class="abs headline cond">Unlock your potential with<br>red light therapy at KorVesta!</h1>
  <p class="abs intro" style="top:228px">Introducing Our New Red Light Therapy Room!</p>
  <p class="abs intro" style="top:304px">Transform Your Wellness Routine with the Power of Light!</p>

  <div class="abs benefits-band"></div>
  <h2 class="abs benefits-title cond">BENEFITS OF RED LIGHT THERAPY</h2>

  <section class="abs benefit" style="top:491px">
    <svg class="benefit-icon" width="22" height="28" viewBox="0 0 22 28" aria-hidden="true"><rect x="0" y="2" width="4" height="24" fill="var(--yellow)"/><rect x="7" y="0" width="5" height="28" fill="var(--yellow)"/><rect x="15" y="6" width="3" height="16" fill="var(--yellow)"/></svg>
    <h3>Boosts Energy Levels</h3>
    <p>Feel revitalized and more energetic after each session.</p>
  </section>
  <section class="abs benefit" style="top:589px">
    <svg class="benefit-icon" width="22" height="28" viewBox="0 0 22 28" aria-hidden="true"><rect x="0" y="2" width="4" height="24" fill="var(--yellow)"/><rect x="7" y="0" width="5" height="28" fill="var(--yellow)"/><rect x="15" y="6" width="3" height="16" fill="var(--yellow)"/></svg>
    <h3>Enhances Muscle Recovery</h3>
    <p>Speed up recovery times post-workout and reduce soreness</p>
  </section>
  <section class="abs benefit" style="top:687px">
    <svg class="benefit-icon" width="22" height="28" viewBox="0 0 22 28" aria-hidden="true"><rect x="0" y="2" width="4" height="24" fill="var(--yellow)"/><rect x="7" y="0" width="5" height="28" fill="var(--yellow)"/><rect x="15" y="6" width="3" height="16" fill="var(--yellow)"/></svg>
    <h3>Improves Skin Health</h3>
    <p>Reduce wrinkles, blemishes, and promote a youthful glow</p>
  </section>
  <section class="abs benefit" style="top:784px">
    <svg class="benefit-icon" width="22" height="28" viewBox="0 0 22 28" aria-hidden="true"><rect x="0" y="2" width="4" height="24" fill="var(--yellow)"/><rect x="7" y="0" width="5" height="28" fill="var(--yellow)"/><rect x="15" y="6" width="3" height="16" fill="var(--yellow)"/></svg>
    <h3>Supports Joint Health</h3>
    <p style="max-width:400px">Alleviate pain and inflammation, making movement easier.</p>
  </section>
  <section class="abs benefit" style="top:882px">
    <svg class="benefit-icon" width="22" height="28" viewBox="0 0 22 28" aria-hidden="true"><rect x="0" y="2" width="4" height="24" fill="var(--yellow)"/><rect x="7" y="0" width="5" height="28" fill="var(--yellow)"/><rect x="15" y="6" width="3" height="16" fill="var(--yellow)"/></svg>
    <h3>Promotes Better Sleep</h3>
    <p>Improve your sleep patterns and overall restfulness</p>
  </section>
  <section class="abs benefit" style="top:980px">
    <svg class="benefit-icon" width="22" height="28" viewBox="0 0 22 28" aria-hidden="true"><rect x="0" y="2" width="4" height="24" fill="var(--yellow)"/><rect x="7" y="0" width="5" height="28" fill="var(--yellow)"/><rect x="15" y="6" width="3" height="16" fill="var(--yellow)"/></svg>
    <h3>Increases Circulation</h3>
    <p style="max-width:400px">Enhance blood flow for better nutrient delivery to muscles.</p>
  </section>

  <div class="abs divider" style="left:520px;top:546px;height:487px"></div>
  <div class="abs divider" style="left:528px;top:582px;height:487px"></div>

  <div class="abs offer offer-first">
    <div class="lead">Try Your First<br>Session for</div>
    <div class="just">Just</div>
    <div class="price">$25</div>
    <div class="regular">Regularly $55</div>
  </div>

  <div class="abs offer offer-limited">
    <div class="lead">Limited Time<br>Only!</div>
    <p>Book your session today and discover how Red Light Therapy can elevate your fitness journey.</p>
  </div>

  <h2 class="abs why-title cond">WHY CHOOSE KORVESTA?</h2>

  <section class="abs reason" style="top:651px">
    <h3>State-of-the-Art Equipment</h3>
    <p>Experience the power of eight Quorvane Glow Therapy TelaRix 700 panels—some of the best on the market!</p>
  </section>
  <div class="abs reason-icon" style="top:637px">
    <svg width="56" height="56" viewBox="0 0 56 56" aria-hidden="true"><circle cx="24" cy="24" r="15" fill="none" stroke="var(--yellow)" stroke-width="7" stroke-dasharray="6 4"/><circle cx="24" cy="24" r="8" fill="none" stroke="var(--yellow)" stroke-width="4"/><line x1="32" y1="32" x2="50" y2="50" stroke="var(--yellow)" stroke-width="7" stroke-linecap="round"/></svg>
  </div>

  <section class="abs reason" style="top:782px">
    <h3>Expert Guidance</h3>
    <p>Our trained staff will guide you through each session to ensure you get the most out of your therapy.</p>
  </section>
  <div class="abs reason-icon" style="top:769px">
    <svg width="56" height="56" viewBox="0 0 56 56" aria-hidden="true"><circle cx="10" cy="9" r="6" fill="var(--yellow)"/><path d="M2 18h16l8 8-3 3-5-5v30H4V30H2z" fill="var(--yellow)"/><rect x="24" y="10" width="30" height="44" rx="2" fill="var(--yellow)"/><g stroke="var(--panel)" stroke-width="3"><line x1="30" y1="20" x2="48" y2="20"/><line x1="30" y1="30" x2="48" y2="30"/><line x1="30" y1="40" x2="48" y2="40"/></g></svg>
  </div>

  <section class="abs reason" style="top:913px">
    <h3>Community Focused</h3>
    <p>Join a supportive community that<br>prioritizes health and wellness.</p>
  </section>
  <div class="abs reason-icon" style="top:900px">
    <svg width="56" height="56" viewBox="0 0 56 56" aria-hidden="true"><circle cx="26" cy="30" r="22" fill="none" stroke="var(--yellow)" stroke-width="6"/><circle cx="26" cy="30" r="12" fill="none" stroke="var(--yellow)" stroke-width="6"/><circle cx="26" cy="30" r="4" fill="var(--yellow)"/><line x1="26" y1="30" x2="48" y2="8" stroke="var(--yellow)" stroke-width="5"/><path d="M44 2l10 0-2 10z" fill="var(--yellow)"/></svg>
  </div>

  <svg class="abs prices" viewBox="0 0 430 120" aria-hidden="true"><polygon points="41,0 430,0 430,120 0,120" fill="var(--charcoal)"/></svg>
  <table class="abs price-table">
    <tr><td class="item">Single Session</td><td class="mem">$35(mem)</td><td>$55(non)</td></tr>
    <tr><td class="item">3 – Pack</td><td class="mem">$102(mem)</td><td>$159(non)</td></tr>
    <tr><td class="item">5 – Pack</td><td class="mem">$167(mem)</td><td>$259(non)</td></tr>
    <tr><td class="item">10 – Pack</td><td class="mem">$316(mem)</td><td>$491(non)</td></tr>
  </table>

  <svg class="abs cta" viewBox="0 0 530 98" aria-hidden="true"><polygon points="0,0 483,0 528,98 0,98" fill="var(--yellow)"/></svg>
  <div class="abs cta-copy">
    <h4>READY TO SHINE?</h4>
    <div class="line">Visit our front desk or call us at</div>
    <div><span class="phone">(555) 014- 2278</span> <span class="after">to schedule your appointment.</span></div>
  </div>

  <footer class="abs footer"><span>KorVesta Fitness Facility</span><span>/</span><span>Your Wellness, Our Commitment!</span></footer>
</main>
</body>
</html>
```